依頼詳細
新規開院に併せて内覧会を開催いたします。
その告知用に折込チラシの配布・ポスティング配布を実施します。
地域の皆様に開院を広く知っていただけるようなシンプルかつインパクトのある、わかりやすいチラシデザインをお願いいたします。ベースのカラーはピンク系が希望です。
女性・高齢者の方に院を知っていただき、アピールできるようなデザインをお願いいたします。
記載項目
・院名/住所/電話番号/施術受付時間/地図/院長よりメッセージなど。
・内覧会開催のお知らせ、開催日(変更になる可能性があります)
・オープンに先がけて内覧会を開催します。
・実際のオープン日など(変更になる可能性があります)
サイズ
A4
ページ数
片面
希望イメージ
シンプル 複雑
単色 カラフル
暗い 明るい
日常 高級
遊び心 厳粛
未来的 伝統的
女性的 男性的
希望する色
赤系、ピンクを中心にお願いいたします。
納品ファイル
• 高解像度JPG (.jpg)
• イラストレーター形式 (.ai)
補足説明
新規開業の接骨院の為、地域の皆様に認知していただけるような親しみがあり、インパクトのあるチラシデザインをお願いいたします。

シンプルでわかりやすいイメージが気に入りました。
地域の皆様に愛される接骨院のイメージが沸きましたので、このデザインに決定いたしました。

たくさんのご提案ありがとうございました。
決定までお時間をいただき申し訳ありませんでしたが、
最初の直感で決定いたしました。またの機会がございましたら
ご提案宜しくお願いいたします。

```html
<!DOCTYPE html>
<html lang="ja">
<head>
<meta charset="UTF-8">
<title>ひかり整骨院 OPEN</title>
<link href="https://fonts.googleapis.com/css2?family=Kosugi+Maru&family=M+PLUS+Rounded+1c:wght@400;700;800&family=Josefin+Sans:wght@400;600&display=swap" rel="stylesheet">
<style>
  :root{
    --bg:#fbe9e6;
    --paper:#fff8f6;
    --pink:#f2b3ad;
    --salmon:#e9877f;
    --rose:#d9645c;
    --brown:#5b4337;
    --line:#e6a6a0;
    --white:#ffffff;
    --map:#e8e2de;
    --illust:#f6d3c9;
  }
  *{margin:0;padding:0;box-sizing:border-box}
  html,body{width:849px;height:1200px;overflow:hidden;background:var(--white)}
  body{font-family:"M PLUS Rounded 1c","Kosugi Maru",sans-serif;color:var(--brown)}
  .flyer{position:relative;width:849px;height:1200px;background:var(--bg);overflow:hidden}
  .abs{position:absolute}

  .clinic-title{left:40px;top:18px;font-size:54px;font-weight:400;letter-spacing:4px;color:var(--brown)}
  .title-rule{left:30px;top:92px;width:540px;height:3px;background:var(--salmon)}
  .hero-illust{left:595px;top:14px;width:225px;height:186px;border-radius:12px;background:linear-gradient(160deg,var(--illust),var(--pink))}

  .open-word{left:50px;top:104px;font-family:"Josefin Sans",sans-serif;font-weight:400;font-size:140px;letter-spacing:14px;line-height:1;color:var(--brown)}
  .open-rule{left:30px;top:234px;width:540px;height:2px;background:var(--brown)}
  .open-date{left:55px;top:244px;font-size:48px;font-weight:700;color:var(--brown);letter-spacing:1px}
  .open-date small{font-size:30px}
  .open-date .dow{display:inline-block;background:var(--brown);color:var(--white);font-size:26px;width:38px;height:38px;line-height:38px;text-align:center;border-radius:4px;vertical-align:middle;margin-left:4px}

  .preview{left:595px;top:212px;width:225px;background:var(--white);border:3px solid var(--pink);border-radius:6px;padding-bottom:10px}
  .preview-head{background:var(--salmon);color:var(--white);font-size:26px;font-weight:700;text-align:center;padding:4px 0;letter-spacing:2px}
  .preview-row{display:flex;align-items:center;gap:8px;margin:8px 12px 0}
  .preview-tag{background:var(--salmon);color:var(--white);font-size:13px;width:24px;border-radius:4px;text-align:center;padding:3px 0;line-height:1.15}
  .preview-val{font-size:22px;color:var(--rose);font-weight:700}
  .preview-val small{font-size:14px}
  .preview-note{margin:8px 14px 0;font-size:12px;line-height:1.55;color:var(--salmon)}

  .lead{left:40px;top:425px;font-size:25px;line-height:1.6;font-weight:700;color:var(--brown)}

  .sec-head{display:flex;align-items:center;height:52px;font-size:32px;font-weight:800;color:var(--salmon);letter-spacing:6px}
  .sec-head .first{background:var(--salmon);color:var(--white);width:52px;height:52px;line-height:52px;text-align:center;border-radius:4px;margin-right:4px}
  .menu-head{left:28px;top:518px;width:527px;border-bottom:2px solid var(--salmon)}
  .menu-list{left:34px;top:582px;display:grid;grid-template-columns:repeat(3,auto);column-gap:26px;row-gap:10px;font-size:17px;color:var(--brown)}
  .menu-list li{list-style:none;display:flex;align-items:center;gap:6px}
  .menu-list svg{flex:none}
  .menu-note{left:34px;top:690px;width:520px;font-size:13px;line-height:1.6;color:var(--salmon)}
  .doctor-illust{left:700px;top:410px;width:110px;height:42px;border-radius:10px;background:linear-gradient(160deg,var(--illust),var(--pink))}

  .hours-head{left:575px;top:455px;width:245px;border-bottom:2px solid var(--salmon)}
  .hours{left:575px;top:515px;width:245px;border-collapse:collapse;background:var(--white);font-size:12px;table-layout:fixed}
  .hours th,.hours td{border:1px solid var(--line);text-align:center;height:34px;font-weight:400;padding:0}
  .hours thead th{background:var(--paper);color:var(--brown)}
  .hours .c-label{width:32px}
  .hours .c-time{width:80px}
  .hours td.time{font-size:11px}
  .hours td.mark{color:var(--salmon);font-size:12px}
  .hours-note{left:575px;top:622px;font-size:11px;color:var(--brown)}

  .greet-head{left:28px;top:740px;width:527px;font-size:26px;font-weight:800;color:var(--salmon);letter-spacing:3px;border-bottom:2px solid var(--salmon);padding-bottom:4px}
  .greet-card{left:28px;top:790px;width:527px;height:192px;background:var(--white);border:8px solid var(--pink);padding:16px 22px}
  .greet-text{font-size:16px;line-height:1.8;color:var(--brown)}
  .greet-sign{position:absolute;left:22px;bottom:10px;font-size:13px;color:var(--brown)}

  .map{left:575px;top:645px;width:245px;height:545px;border-radius:4px;background:linear-gradient(150deg,var(--map),#f1ece8)}

  .footer{left:0;top:990px;width:555px;height:210px;background:var(--salmon);color:var(--white);padding:22px 32px}
  .footer-name{font-size:46px;letter-spacing:6px;font-weight:400}
  .footer-addr{font-size:14px;margin-top:6px;line-height:1.5}
  .footer-tel{display:flex;align-items:center;gap:10px;font-family:"Josefin Sans",sans-serif;font-size:42px;font-weight:600;margin-top:8px}
</style>
</head>
<body>
<main class="flyer">
  <h1 class="abs clinic-title">ひかり整骨院</h1>
  <div class="abs title-rule"></div>
  <div class="abs hero-illust" role="img" aria-label="施術台で患者に施術する柔道整復師のイラスト"></div>

  <div class="abs open-word">OPEN</div>
  <div class="abs open-rule"></div>
  <div class="abs open-date">2015<small>年</small>0<small>月</small>00<small>日</small><span class="dow">月</span></div>

  <section class="abs preview">
    <div class="preview-head">内覧会開催</div>
    <div class="preview-row"><span class="preview-tag">日時</span><span class="preview-val">0月00日<small>(月)</small></span></div>
    <div class="preview-row"><span class="preview-tag" style="visibility:hidden">時</span><span class="preview-val">00:00〜00:00</span></div>
    <p class="preview-note">院内オープン前に、<br>内覧会を開催します。<br>お気軽にお越しください。</p>
  </section>

  <p class="abs lead">患者様1人1人に寄り添い、<br>痛みの根本を治す治療を目指しています。</p>

  <div class="abs doctor-illust" role="img" aria-label="白衣の院長のイラスト"></div>

  <div class="abs sec-head menu-head"><span class="first">施</span>術内容</div>
  <ul class="abs menu-list">
    <li><svg width="16" height="16" viewBox="0 0 16 16"><rect x="1" y="1" width="14" height="14" fill="none" stroke="#5b4337" stroke-width="1.5"/><path d="M3 8l4 4 7-9" fill="none" stroke="#d9645c" stroke-width="2"/></svg>交通事故のむちうち</li>
    <li><svg width="16" height="16" viewBox="0 0 16 16"><rect x="1" y="1" width="14" height="14" fill="none" stroke="#5b4337" stroke-width="1.5"/><path d="M3 8l4 4 7-9" fill="none" stroke="#d9645c" stroke-width="2"/></svg>ぎっくり腰</li>
    <li><svg width="16" height="16" viewBox="0 0 16 16"><rect x="1" y="1" width="14" height="14" fill="none" stroke="#5b4337" stroke-width="1.5"/><path d="M3 8l4 4 7-9" fill="none" stroke="#d9645c" stroke-width="2"/></svg>捻挫</li>
    <li><svg width="16" height="16" viewBox="0 0 16 16"><rect x="1" y="1" width="14" height="14" fill="none" stroke="#5b4337" stroke-width="1.5"/><path d="M3 8l4 4 7-9" fill="none" stroke="#d9645c" stroke-width="2"/></svg>交通事故のむちうち</li>
    <li><svg width="16" height="16" viewBox="0 0 16 16"><rect x="1" y="1" width="14" height="14" fill="none" stroke="#5b4337" stroke-width="1.5"/><path d="M3 8l4 4 7-9" fill="none" stroke="#d9645c" stroke-width="2"/></svg>ぎっくり腰</li>
    <li><svg width="16" height="16" viewBox="0 0 16 16"><rect x="1" y="1" width="14" height="14" fill="none" stroke="#5b4337" stroke-width="1.5"/><path d="M3 8l4 4 7-9" fill="none" stroke="#d9645c" stroke-width="2"/></svg>捻挫</li>
    <li><svg width="16" height="16" viewBox="0 0 16 16"><rect x="1" y="1" width="14" height="14" fill="none" stroke="#5b4337" stroke-width="1.5"/><path d="M3 8l4 4 7-9" fill="none" stroke="#d9645c" stroke-width="2"/></svg>交通事故のむちうち</li>
    <li><svg width="16" height="16" viewBox="0 0 16 16"><rect x="1" y="1" width="14" height="14" fill="none" stroke="#5b4337" stroke-width="1.5"/><path d="M3 8l4 4 7-9" fill="none" stroke="#d9645c" stroke-width="2"/></svg>ぎっくり腰</li>
    <li><svg width="16" height="16" viewBox="0 0 16 16"><rect x="1" y="1" width="14" height="14" fill="none" stroke="#5b4337" stroke-width="1.5"/><path d="M3 8l4 4 7-9" fill="none" stroke="#d9645c" stroke-width="2"/></svg>捻挫</li>
  </ul>
  <p class="abs menu-note">各種保険取扱い。交通事故の施術にも対応しております。<br>痛みや不調のことなど、お気軽にご相談ください。</p>

  <div class="abs sec-head hours-head"><span class="first">診</span>療時間</div>
  <table class="abs hours">
    <colgroup><col class="c-label"><col class="c-time"><col><col><col><col><col><col><col></colgroup>
    <thead><tr><th></th><th>時間</th><th>月</th><th>火</th><th>水</th><th>木</th><th>金</th><th>土</th><th>日</th></tr></thead>
    <tbody>
      <tr><th>午前</th><td class="time">00:00〜00:00</td><td class="mark">●</td><td class="mark">●</td><td class="mark">●</td><td class="mark">●</td><td class="mark">●</td><td class="mark">●</td><td>−</td></tr>
      <tr><th>午後</th><td class="time">00:00〜00:00</td><td class="mark">●</td><td class="mark">●</td><td class="mark">●</td><td class="mark">●</td><td class="mark">●</td><td>−</td><td>−</td></tr>
    </tbody>
  </table>
  <p class="abs hours-note">※休診日・・・日曜日・祝日</p>

  <div class="abs map" role="img" aria-label="ひかり整骨院周辺の案内地図"></div>

  <h2 class="abs greet-head">院長よりごあいさつ</h2>
  <section class="abs greet-card">
    <p class="greet-text">このたび、地域の皆様の健康をお支えするため整骨院を開院いたしました。痛みの原因を丁寧に探り、一人ひとりに合った施術をご提案いたします。どうぞお気軽にご来院ください。</p>
    <p class="greet-sign">ひかり整骨院 院長</p>
  </section>

  <footer class="abs footer">
    <div class="footer-name">ひかり整骨院</div>
    <div class="footer-addr">〒000-0000<br>東京都○○区○○町0-0-0</div>
    <div class="footer-tel">
      <svg width="34" height="34" viewBox="0 0 24 24"><path fill="#ffffff" d="M6.6 10.8a15 15 0 006.6 6.6l2.2-2.2a1 1 0 011-.25 11.4 11.4 0 003.6.6 1 1 0 011 1V20a1 1 0 01-1 1A17 17 0 013 4a1 1 0 011-1h3.5a1 1 0 011 1c0 1.25.2 2.45.57 3.57a1 1 0 01-.25 1z"/></svg>
      000-000-0000
    </div>
  </footer>
</main>
</body>
</html>
```